New business card design to go with our new logo

just want an eye-catching business card to go with our new logo. We are open to double sided or single sided. Just want it to have the following info on it. Whatever layout you think looks best.

First and Last Name
Title
Phone 801-555-0187
Address 312 W. Larkmoor Avenue Orem UT 84057
Email thecrew@meadowstailandkennel.example

Industry/Entity Type

Business

```html
<!DOCTYPE html>
<html lang="en">
<head>
<meta charset="utf-8">
<title>Meadows Tail &amp; Kennel — Business Card</title>
<link rel="stylesheet" href="https://fonts.googleapis.com/css2?family=Roboto:wght@400;500&family=Fira+Sans:wght@500&display=swap">
<style>
  :root {
    --backdrop: #bdbdbd;
    --brand-blue: #1f9fd4;
    --brand-blue-deep: #1588c0;
    --brand-orange: #e07b3c;
    --card-white: #f6f6f6;
    --ink-white: #ffffff;
  }
  * { margin: 0; padding: 0; box-sizing: border-box; }
  html, body { width: 1200px; height: 576px; overflow: hidden; }
  body {
    background: var(--backdrop);
    font-family: "Roboto", Arial, sans-serif;
    position: relative;
  }
  .card {
    position: absolute;
    top: 138px;
    width: 484px;
    height: 293px;
    border-radius: 12px;
    overflow: hidden;
  }
  .card--front {
    left: 82px;
    background: linear-gradient(135deg, var(--brand-blue) 0%, var(--brand-blue-deep) 100%);
  }
  .card--back {
    left: 602px;
    background: var(--card-white);
  }

  /* Front */
  .front-name {
    position: absolute;
    left: 0; right: 0; top: 122px;
    text-align: center;
    color: var(--ink-white);
    font-weight: 500;
    font-size: 30px;
    letter-spacing: 0.5px;
  }

  /* Back */
  .back-wave { position: absolute; inset: 0; width: 100%; height: 100%; }
  .brand-lockup {
    position: absolute;
    left: 28px; top: 34px;
    display: flex; align-items: center; gap: 18px;
  }
  .brand-mark {
    width: 78px; height: 78px;
    border-radius: 50%;
    border: 4px solid var(--brand-orange);
  }
  .brand-name {
    color: var(--brand-orange);
    font-weight: 500;
    font-size: 25px;
    line-height: 1.1;
  }
  .person {
    position: absolute;
    left: 22px; top: 232px;
    color: var(--ink-white);
  }
  .person-name {
    font-family: "Fira Sans", Arial, sans-serif;
    font-weight: 500;
    font-size: 19px;
  }
  .person-title { font-size: 12px; margin-top: 4px; }
  .contact {
    position: absolute;
    right: 14px; top: 180px;
    color: var(--ink-white);
    font-size: 12.5px;
    text-align: right;
    line-height: 18px;
  }
  .contact-address { margin-right: 17px; margin-bottom: 3px; }
  .contact-row { display: flex; justify-content: flex-end; align-items: center; gap: 6px; }
  .contact-icon { width: 11px; height: 11px; flex: none; }
</style>
</head>
<body>
  <section class="card card--front">
    <div class="front-name">Meadows Tail &amp; Kennel</div>
  </section>

  <section class="card card--back">
    <svg class="back-wave" viewBox="0 0 484 293" preserveAspectRatio="none" aria-hidden="true">
      <path d="M0,148 C80,165 150,212 210,212 C290,212 380,130 484,115 L484,293 L0,293 Z" fill="var(--brand-blue)"/>
      <path d="M0,136 C80,153 150,198 210,198 C290,198 380,112 484,96 L484,108 C380,122 290,206 210,206 C150,206 80,160 0,144 Z" fill="var(--brand-orange)"/>
    </svg>

    <div class="brand-lockup">
      <span class="brand-mark"></span>
      <span class="brand-name">Meadows Tail<br>&amp; Kennel</span>
    </div>

    <div class="person">
      <div class="person-name">John Doe Smith</div>
      <div class="person-title">Managing Director</div>
    </div>

    <div class="contact">
      <div class="contact-address">312 W. Larkmoor Avenue<br>Orem UT 84057</div>
      <div class="contact-row">801-555-0187
        <svg class="contact-icon" viewBox="0 0 12 12"><path d="M2,1 L4.5,1 L5.5,3.5 L4,4.5 C4.6,6 6,7.4 7.5,8 L8.5,6.5 L11,7.5 L11,10 C6,10.5 1.5,6 2,1 Z" fill="currentColor"/></svg>
      </div>
      <div class="contact-row">www.meadowstailandkennel.example
        <svg class="contact-icon" viewBox="0 0 12 12"><circle cx="6" cy="6" r="5" fill="none" stroke="currentColor" stroke-width="1.2"/><path d="M1,6 H11 M6,1 C3,4 3,8 6,11 M6,1 C9,4 9,8 6,11" fill="none" stroke="currentColor" stroke-width="1"/></svg>
      </div>
      <div class="contact-row">thecrew@meadowstailandkennel.example
        <svg class="contact-icon" viewBox="0 0 12 12"><rect x="1" y="2.5" width="10" height="7" fill="currentColor"/><path d="M1,2.5 L6,6.5 L11,2.5" fill="none" stroke="var(--brand-blue)" stroke-width="1"/></svg>
      </div>
    </div>
  </section>
</body>
</html>
```